Two Bodyguards

Cover for a book in French language:
- Author: Gérard Mabille-Fournet
- Title: Quiet rooms rarely keep their secrets
- Publisher (at the bottom of the page): Editions Varouze
Key Words:
- a rich man died recently, it looks like a murder. He has been found in his luxury apartment.
- Two Body Guards: one is elegant, the other a bit fat.
- two pretty women.
- Inheritance (wealth)
Size of the cover: 14 x 20.5 cm (+ bleed area)
Please note that the title should remain in English: "Stiff guests seldom leave on time".
By the way the title doesn't mean anything. It's just a joke.
Thrillers' reader

```html
<!DOCTYPE html>
<html lang="en">
<head>
<meta charset="utf-8">
<title>Quiet rooms rarely keep their secrets — Gérard Mabille-Fournet</title>
<link rel="stylesheet" href="https://fonts.googleapis.com/css2?family=Cinzel:wght@400&family=Ephesis&family=Open+Sans:wght@400&display=swap">
<style>
  :root {
    --night: #141b2e;
    --storm: #1c3440;
    --teal: #2f5258;
    --haze: #c9d3a8;
    --slate: #25333f;
    --shadow: #0a0f19;
    --ink-light: #ffffff;
  }
  html, body {
    margin: 0;
    padding: 0;
    width: 819px;
    height: 1200px;
    overflow: hidden;
    background: var(--night);
  }
  .cover {
    position: relative;
    width: 819px;
    height: 1200px;
    overflow: hidden;
  }
  .cover-scene {
    position: absolute;
    inset: 0;
    background:
      /* dark foreground masses: two standing figures and the tower between them */
      radial-gradient(ellipse 150px 420px at 215px 1010px, rgba(8, 12, 20, 0.95), rgba(8, 12, 20, 0) 75%),
      radial-gradient(ellipse 150px 420px at 625px 1010px, rgba(8, 12, 20, 0.95), rgba(8, 12, 20, 0) 75%),
      radial-gradient(ellipse 260px 420px at 420px 860px, rgba(22, 38, 48, 0.9), rgba(22, 38, 48, 0) 75%),
      /* pale light breaking through the clouds */
      radial-gradient(ellipse 360px 200px at 110px 640px, rgba(222, 228, 182, 0.95), rgba(222, 228, 182, 0) 72%),
      radial-gradient(ellipse 300px 170px at 330px 470px, rgba(190, 204, 168, 0.55), rgba(190, 204, 168, 0) 72%),
      radial-gradient(ellipse 220px 180px at 760px 720px, rgba(170, 190, 160, 0.5), rgba(170, 190, 160, 0) 72%),
      linear-gradient(180deg,
        var(--night) 0%,
        var(--night) 12%,
        var(--storm) 26%,
        var(--teal) 40%,
        #5d7770 52%,
        #3b5057 64%,
        var(--slate) 76%,
        var(--shadow) 100%);
  }
  .author {
    position: absolute;
    top: 36px;
    left: 0;
    right: 0;
    margin: 0;
    text-align: center;
    font-family: "Cinzel", serif;
    font-weight: 400;
    font-size: 35px;
    letter-spacing: 8px;
    color: var(--ink-light);
  }
  .title {
    position: absolute;
    top: 196px;
    left: 0;
    right: 0;
    margin: 0;
    text-align: center;
    font-family: "Ephesis", cursive;
    font-weight: 400;
    font-size: 118px;
    line-height: 92px;
    color: var(--ink-light);
  }
  .title span { display: block; }
  .publisher {
    position: absolute;
    top: 1098px;
    left: 0;
    right: 0;
    margin: 0;
    text-align: center;
    font-family: "Open Sans", sans-serif;
    font-size: 29px;
    color: var(--ink-light);
  }
</style>
</head>
<body>
  <main class="cover">
    <div class="cover-scene" role="img" aria-label="Photograph: two bodyguards seen from behind as dark silhouettes, one elegant and one heavier, standing before a tall luxury apartment tower under a stormy teal sky with pale light breaking through the clouds"></div>
    <p class="author">Gérard Mabille-Fournet</p>
    <h1 class="title">
      <span>Quiet rooms</span>
      <span>rarely keep</span>
      <span>their secrets</span>
    </h1>
    <p class="publisher">Editions Varouze</p>
  </main>
</body>
</html>
```